Visitenkarten
Zielgruppe
Wir handeln und restaurieren (mit) sehr hochwertigen Fahrzeugen (Oldtimier/Supercars) bis in den Bereich von mehreren Millionen Euro. Die Zielgruppe sind potentielle Käufer im sehr gehobenen Premium Segment.
Aufgabenstellung
Eine Visitenkarte im Idealfall mit dem schwarzen Logo soll erstellt werden. Standardformat oder ein kreatives, aber praktikables Format. Ziel ist eine sehr hochwertige, geprägte Visitenkarte. Frontseite das Velvet Marques Logo, Rückseite einmal: Jonas Wehrberg, Owner, Phone +436601742863, Email Sales@velvet-marques.com Salzburg Dobrovnik (generisch anpassbare Adresse)

```html
<!DOCTYPE html>
<html lang="de">
<head>
<meta charset="utf-8">
<title>Velvet Marques – Visitenkarten</title>
<link rel="stylesheet" href="https://fonts.googleapis.com/css2?family=Libre+Baskerville:wght@400;700&display=swap">
<style>
  :root {
    --backdrop: #cacaca;
    --card: #f9f9f9;
    --ink: #3a3a3a;
    --ink-strong: #262626;
    --muted: #9a9a9a;
    --rule: #6a6a6a;
    --shadow: rgba(0, 0, 0, 0.18);
  }
  * { box-sizing: border-box; margin: 0; padding: 0; }
  html, body {
    width: 1200px;
    height: 554px;
    overflow: hidden;
    background: var(--backdrop);
    font-family: "Libre Baskerville", Georgia, serif;
    color: var(--ink);
  }
  .stage {
    width: 1200px;
    height: 554px;
    display: flex;
    align-items: center;
    justify-content: center;
    gap: 60px;
  }
  .card {
    width: 440px;
    height: 286px;
    background: var(--card);
    box-shadow: 0 6px 18px var(--shadow);
    display: flex;
    flex-direction: column;
    align-items: center;
    justify-content: center;
  }
  .brand {
    display: flex;
    align-items: center;
    gap: 14px;
  }
  .brand-dot {
    width: 30px;
    height: 30px;
    border-radius: 50%;
    background: var(--ink);
  }
  .brand-name {
    font-size: 25px;
    font-weight: 400;
    letter-spacing: 0.08em;
    text-transform: uppercase;
    color: var(--ink);
  }
  .contact {
    text-align: center;
  }
  .contact-dot {
    width: 16px;
    height: 16px;
    border-radius: 50%;
    background: var(--ink);
    margin: 0 auto 10px;
  }
  .person-name {
    font-size: 15px;
    font-weight: 700;
    color: var(--ink-strong);
  }
  .person-role {
    font-size: 9px;
    color: var(--muted);
    margin-top: 3px;
  }
  .divider {
    width: 1px;
    height: 30px;
    background: var(--rule);
    margin: 12px auto;
  }
  .details {
    list-style: none;
    font-size: 11px;
    line-height: 1.55;
    color: var(--ink);
  }
</style>
</head>
<body>
  <main class="stage">
    <section class="card card-front" aria-label="Vorderseite">
      <div class="brand">
        <span class="brand-dot" aria-hidden="true"></span>
        <span class="brand-name">Velvet Marques</span>
      </div>
    </section>

    <section class="card card-back" aria-label="Rückseite">
      <div class="contact">
        <div class="contact-dot" aria-hidden="true"></div>
        <p class="person-name">Jonas Wehrberg</p>
        <p class="person-role">Owner</p>
        <div class="divider" aria-hidden="true"></div>
        <ul class="details">
          <li>+436601742863</li>
          <li>Sales@velvet-marques.com</li>
          <li>Lindenau | Korvara</li>
        </ul>
      </div>
    </section>
  </main>
</body>
</html>
```